Very Simple/Minimal Business Card Design Project

The company operates in the industrial maritime infrastructure sector in Brazil. You can find more information on our website www.navelquor.com.br WE NEED TO LOOK POWERFUL AND SERIOUS
I have attached a copy of the old cards. We would like something more professional / industrial / sexy that also includes the position.

The card can be double sided or not. We would like you to propose as many options.

Thank you
Updates

Many thanks, do let me know if you have any questions. I am under a lot of time pressure to try and have them printed over the next days or so.

Please could you use the following information

for the address: Rua Tapiraçu, 418 - Centro, Rio de Janeiro, 20135-070, Brasil

for the mobile: +55 21 8372 9041
for the landline: +55 21 4067 3859

and position:  Diretor Geral

Thakn you

Target Market(s)

Shipowners, bankers, industrial companies

Industry/Entity Type

Industrial

Requirements
Must have
• POWERFUL
SERIOUS
SOLID
BIG CORPORATION

```html
<!DOCTYPE html>
<html lang="pt-BR">
<head>
<meta charset="utf-8">
<title>Navelquor – Cartão de visita</title>
<link rel="stylesheet" href="https://fonts.googleapis.com/css2?family=Arimo:wght@700&family=Mulish:wght@400;700;800&display=swap">
<style>
  :root {
    --stage: #3a3a3a;
    --amber: #ffb800;
    --amber-light: #ffcc00;
    --navy: #0f2a7a;
    --green: #1a9a3c;
    --lavender: #dcdfea;
    --mint: #dff0e2;
    --white: #ffffff;
  }
  * { margin: 0; padding: 0; box-sizing: border-box; }
  html, body { width: 1200px; height: 900px; overflow: hidden; }
  body { background: var(--stage); position: relative; font-family: "Mulish", sans-serif; }

  .card {
    position: absolute;
    top: 295px;
    width: 509px;
    height: 308px;
    border-radius: 20px;
    overflow: hidden;
    box-shadow: 0 6px 16px rgba(0,0,0,.35);
  }
  .card--front { left: 77px; background: var(--amber); }
  .card--back { left: 616px; background: var(--white); }
  .card__bg { position: absolute; inset: 0; width: 100%; height: 100%; }

  .brand { position: absolute; display: flex; align-items: center; }
  .brand__mark { background: var(--navy); }
  .brand__name {
    font-family: "Arimo", sans-serif;
    font-weight: 700;
    color: var(--navy);
    letter-spacing: 0.5px;
    line-height: 1;
  }
  .card--front .brand { left: 83px; top: 126px; gap: 10px; }
  .card--front .brand__mark { width: 68px; height: 68px; border-radius: 5px; }
  .card--front .brand__name { font-size: 45px; }

  .card--back .brand { left: 110px; top: 27px; gap: 8px; }
  .card--back .brand__mark { width: 56px; height: 56px; border-radius: 4px; }
  .card--back .brand__name { font-size: 37px; }

  .contact {
    position: absolute;
    left: 0; right: 0; top: 118px;
    text-align: center;
    color: var(--navy);
  }
  .contact__name { font-size: 20px; font-weight: 800; color: var(--green); line-height: 24px; }
  .contact__role { font-size: 12px; font-weight: 700; color: var(--navy); line-height: 16px; margin-bottom: 6px; }
  .contact__list { list-style: none; font-size: 14px; line-height: 18px; }
  .contact__list li { display: flex; justify-content: center; align-items: center; gap: 4px; }
  .contact__icon { width: 10px; height: 10px; fill: var(--green); flex: none; }
  .contact__address { margin-top: 10px; font-size: 13px; font-weight: 700; line-height: 17px; }
</style>
</head>
<body>

<section class="card card--front">
  <svg class="card__bg" viewBox="0 0 509 308" preserveAspectRatio="none" aria-hidden="true">
    <polygon points="0,40 58,0 230,308 135,308" fill="var(--amber-light)"/>
    <polygon points="450,0 509,0 509,60 370,308 275,308" fill="var(--amber-light)"/>
  </svg>
  <div class="brand">
    <span class="brand__mark"></span>
    <span class="brand__name">NAVELQUOR</span>
  </div>
</section>

<section class="card card--back">
  <svg class="card__bg" viewBox="0 0 509 308" preserveAspectRatio="none" aria-hidden="true">
    <polygon points="0,75 0,308 145,308" fill="var(--mint)"/>
    <polygon points="509,65 509,308 375,308" fill="var(--mint)"/>
    <polygon points="58,0 450,0 275,308 240,308" fill="var(--lavender)"/>
  </svg>
  <div class="brand">
    <span class="brand__mark"></span>
    <span class="brand__name">NAVELQUOR</span>
  </div>
  <div class="contact">
    <p class="contact__name">Rafael Monteiro</p>
    <p class="contact__role">Diretor Geral</p>
    <ul class="contact__list">
      <li><svg class="contact__icon" viewBox="0 0 10 10"><circle cx="5" cy="5" r="5"/></svg>+ 55 21 4067 3859</li>
      <li><svg class="contact__icon" viewBox="0 0 10 10"><rect x="2" y="0.7" width="6" height="8.6" rx="1" fill="none" stroke="var(--green)" stroke-width="1.4"/></svg>+ 55 21 8372 9041</li>
      <li><svg class="contact__icon" viewBox="0 0 10 10"><rect x="0" y="2" width="10" height="7"/></svg>rafael@navelquor.com.br</li>
      <li><svg class="contact__icon" viewBox="0 0 10 10"><circle cx="5" cy="5" r="4.3" fill="none" stroke="var(--green)" stroke-width="1.4"/><line x1="0.7" y1="5" x2="9.3" y2="5" stroke="var(--green)" stroke-width="1"/></svg>www.navelquor.com.br</li>
    </ul>
    <p class="contact__address">Rua Tapiraçu, 418 - Centro<br>Rio de Janeiro, 20135-070, Brasil</p>
  </div>
</section>

</body>
</html>
```